Security business needs NDA formatted.

We need our NDA formatted properly and to look modern with our logo. Anybody can paste words into a document, but we need something clean, modern, DocuSign-friendly, and stylish.

```html
<!DOCTYPE html>
<html lang="en">
<head>
<meta charset="utf-8">
<title>Terravue Non-Disclosure Agreement</title>
<link href="https://fonts.googleapis.com/css2?family=Roboto:ital,wght@0,700;0,900;1,700&family=Tinos:wght@400;700&display=swap" rel="stylesheet">
<style>
:root{
  --ink:#2a2a2a;
  --black:#111111;
  --dark:#434343;
  --light:#cdcdcd;
  --faint:#f1f1f1;
  --paper:#ffffff;
}
*{margin:0;padding:0;box-sizing:border-box}
html,body{width:1200px;height:679px;overflow:hidden;background:var(--paper)}
.spread{display:grid;grid-template-columns:repeat(5,240px);grid-template-rows:repeat(2,339.5px);width:1200px;height:679px}
.page{position:relative;overflow:hidden;background:var(--paper);color:var(--ink);font-family:"Tinos","Times New Roman",serif;font-size:4.4px;line-height:6.2px}
.page-art{position:absolute;inset:0;width:240px;height:340px}
.page-number{position:absolute;top:11px;right:22px;font-family:"Roboto",Arial,sans-serif;font-weight:700;font-style:italic;font-size:4.9px;color:var(--black)}
.page-body{position:absolute;top:22px;left:18px;width:206px}
.clause{display:grid;grid-template-columns:13px 1fr;margin-bottom:6px}
.clause.tight{margin-bottom:1px}
.sub{display:grid;grid-template-columns:13px 1fr;margin:0 0 5px 0}
.sub.tight{margin-bottom:0}
.subsub{display:grid;grid-template-columns:13px 1fr;margin:0 0 1px 13px}
.heading{font-weight:700;margin:2px 0 1px}
.heading.underline{text-decoration:underline}
.heading.indent{margin-left:13px}
.justify{text-align:justify}
/* cover */
.brand{position:absolute;top:28px;left:39px;display:flex;align-items:center;gap:5px}
.brand-mark{width:19px;height:19px;border-radius:50%;background:var(--black)}
.brand-name{font-family:"Roboto",Arial,sans-serif;font-weight:700;font-size:10.5px;color:var(--black)}
.cover-title{position:absolute;top:153px;left:0;width:240px;text-align:center;font-family:"Roboto",Arial,sans-serif;font-weight:900;font-size:13.4px;line-height:16px;color:var(--black)}
/* parties page */
.parties{position:absolute;top:44px;left:0;width:240px;text-align:center;font-size:7px;line-height:8.4px}
.parties .title{font-weight:700}
.parties p{margin-bottom:13px}
.parties .strong{font-weight:700}
/* signature */
.witness{position:absolute;top:22px;left:17px;width:210px}
.sign-block{position:absolute;left:110px;font-size:4.6px}
.sign-line{margin-top:11px}
</style>
</head>
<body>
<main class="spread">

<!-- Row 1 -->
<section class="page cover">
  <svg class="page-art" viewBox="0 0 240 340" aria-hidden="true">
    <rect x="0" y="0" width="240" height="120" fill="var(--light)"/>
    <path d="M70,0 H240 V130 H70Z" fill="var(--black)"/>
    <ellipse cx="150" cy="250" rx="200" ry="225" fill="var(--paper)"/>
    <circle cx="37" cy="258" r="62" fill="var(--faint)"/>
    <path d="M240,250 Q226,302 190,340 H240Z" fill="var(--light)"/>
    <path d="M0,293 Q100,265 240,330 V340 H0Z" fill="var(--dark)"/>
    <path d="M240,298 Q226,325 205,340 H240Z" fill="var(--black)"/>
  </svg>
  <div class="brand"><span class="brand-mark"></span><span class="brand-name">Terravue</span></div>
  <h1 class="cover-title">NON-DISCLOSURE<br>AGREEMENT</h1>
</section>

<section class="page">
  <svg class="page-art" viewBox="0 0 240 340" aria-hidden="true">
    <circle cx="37" cy="258" r="62" fill="var(--faint)"/>
    <path d="M240,250 Q226,302 190,340 H240Z" fill="var(--light)"/>
    <path d="M0,300 Q100,270 240,330 V340 H0Z" fill="var(--dark)"/>
    <path d="M240,298 Q226,325 205,340 H240Z" fill="var(--black)"/>
  </svg>
  <div class="page-number">Page 1 of 8</div>
  <div class="page-body">
    <p class="heading">BACKGROUND:</p>
    <div class="clause"><span>A.</span><span>ACME has proprietary information and expertise relating to certain investigation tools and tactics (the "Company").</span></div>
    <div class="clause"><span>B.</span><span>In connection with the Evaluator evaluating the Invention for possible patent, development, and marketing (the "Permitted Purpose"), the Evaluator has requested certain confidential information (the "Confidential Information") regarding the Company.</span></div>
    <p class="heading">IN CONSIDERATION OF</p>
    <p style="margin-bottom:6px">And as a condition of the Company providing the Confidential Information to the Evaluator in addition to other valuable consideration, the receipt and sufficiency of which consideration is hereby acknowledged, the parties to this Agreement agree as follows:</p>
    <p class="heading underline">Confidential Information</p>
    <div class="clause justify"><span>1.</span><span>All written and oral information and materials disclosed or provided by the Company to the Evaluator under this Agreement constitute Confidential Information regardless of whether such information was provided before or after the date of this Agreement or how it was provided to the Evaluator.</span></div>
    <div class="clause tight"><span>2.</span><span>'Confidential Information' means all data and information relating to the invention as well as data and information relating to the Company, including but not limited to, the following:</span></div>
    <div style="margin-left:13px" class="justify">
      <div class="sub"><span>a.</span><span>'Business Operations' which includes internal personnel and financial information of the Company, vendor names and other vendor information (including vendor characteristics, services and agreements), purchasing and internal cost information, internal services and operational manuals, external business contacts including those stored on social media accounts or other similar platforms or databases operated by the Company, and the manner and methods of conducting the Company's business;</span></div>
      <div class="sub"><span>b.</span><span>'Customer Information' which includes names of customers of the Company, their representatives, all customer contact information, contracts and their contents and parties, customer services, data provided by customers and the type, quantity and specifications of products and services purchased, leased, licensed or received by customers of the Company;</span></div>
      <div class="sub"><span>c.</span><span>'Intellectual Property' which includes information relating to the Company's proprietary rights prior to any public disclosure of such information, including but not limited to the nature of the proprietary rights, production data, technical and engineering data, technical concepts, test data and test results, simulation results, the status and details of research and development of products and services, and information regarding acquiring, protecting, enforcing and licensing proprietary rights (including patents, copyrights and trade secrets);</span></div>
    </div>
  </div>
</section>

<section class="page">
  <svg class="page-art" viewBox="0 0 240 340" aria-hidden="true">
    <circle cx="37" cy="258" r="62" fill="var(--faint)"/>
    <path d="M240,250 Q226,302 190,340 H240Z" fill="var(--light)"/>
    <path d="M0,300 Q100,270 240,330 V340 H0Z" fill="var(--dark)"/>
    <path d="M240,298 Q226,325 205,340 H240Z" fill="var(--black)"/>
  </svg>
  <div class="page-number" style="top:14px">Page 3 of 8</div>
  <div class="page-body" style="top:26px">
    <div class="sub" style="margin-left:13px"><span>k.</span><span>Confidential Information will also include any information that has been disclosed by a third party to the Company and is protected by a non-disclosure agreement entered into between the third party and the Company.</span></div>
    <div class="clause tight"><span>3.</span><span>Confidential Information will not include the following information:</span></div>
    <div style="margin-left:13px;margin-bottom:6px">
      <div class="sub tight"><span>a.</span><span>Information that is generally known in the industry of the Company;</span></div>
      <div class="sub tight"><span>b.</span><span>Information that is now or subsequently becomes generally available to the public through no wrongful act of the Evaluator;</span></div>
      <div class="sub tight"><span>c.</span><span>Information rightly in the possession of the Evaluator prior to the disclosure to the Evaluator by the Company;</span></div>
      <div class="sub tight"><span>d.</span><span>Information that is independently created by the Evaluator without direct or indirect use of the Confidential Information; or</span></div>
      <div class="sub tight"><span>e.</span><span>Information that the Evaluator rightfully obtains from a third party who has the right to transfer or disclose it.</span></div>
    </div>
    <p class="heading">Obligations of Non-Disclosure</p>
    <div class="clause"><span>4.</span><span>Except as otherwise provided in this Agreement, the Evaluator must not disclose the Confidential Information.</span></div>
    <div class="clause"><span>5.</span><span>Except as otherwise provided in this Agreement, the Confidential Information will remain the exclusive property of the Company and will only be used by the Evaluator for the Permitted Purpose. The Evaluator will not use the Confidential Information for any purpose that might be directly or indirectly detrimental to the Company or any associated affiliates or subsidiaries.</span></div>
    <div class="clause"><span>6.</span><span>The obligations to ensure and prevent the disclosure of the Confidential Information imposed on the Evaluator in this Agreement and any obligations to provide notice under this Agreement will survive the expiration or termination, as the case may be, of this Agreement and those obligations will last indefinitely.</span></div>
    <div class="clause tight"><span>7.</span><span>The Evaluator may disclose any of the Confidential Information:</span></div>
    <div class="sub" style="margin-left:13px;margin-bottom:3px"><span>a.</span><span>To such employees, agents, representatives and advisors of the Evaluator that have a need to know for the Permitted Purpose provided that:</span></div>
    <div class="subsub"><span>i.</span><span>The Evaluator has informed such personnel of the confidential nature of the Confidential Information;</span></div>
    <div class="subsub"><span>ii.</span><span>Such personnel agree to be legally bound to the same burdens of non-disclosure and non-use as the Evaluator;</span></div>
    <div class="subsub"><span>iii.</span><span>The Evaluator agrees to take all necessary steps to ensure that the terms of this Agreement are not violated by such personnel; and</span></div>
    <div class="subsub"><span>iv.</span><span>The Evaluator agrees to be responsible for and indemnify the Company for any breach of this Agreement by its personnel.</span></div>
  </div>
</section>

<section class="page">
  <svg class="page-art" viewBox="0 0 240 340" aria-hidden="true">
    <circle cx="37" cy="258" r="62" fill="var(--faint)"/>
    <path d="M240,250 Q226,302 190,340 H240Z" fill="var(--light)"/>
    <path d="M0,300 Q100,270 240,330 V340 H0Z" fill="var(--dark)"/>
    <path d="M240,298 Q226,325 205,340 H240Z" fill="var(--black)"/>
  </svg>
  <div class="page-number" style="top:17px">Page 5 of 8</div>
  <div class="page-body" style="top:26px;left:20px;width:200px">
    <div style="margin-left:13px;margin-bottom:6px">
      <div class="sub tight"><span>a.</span><span>Return all Confidential Information to the Company;</span></div>
      <div class="sub tight"><span>b.</span><span>Provide a certificate to the Company to the effect that the Evaluator has returned all Confidential Information to the Company.</span></div>
    </div>
    <p class="heading indent">Notices</p>
    <div class="clause"><span>14.</span><span>In the event that the Evaluator is required in a civil, criminal or regulatory proceeding to disclose any part of the Confidential Information, the Evaluator will give to the Company prompt written notice of such request so the Company may seek an appropriate remedy or alternatively to waive the Evaluator's compliance with the provisions of this Agreement in regards to the request.</span></div>
    <div class="clause"><span>15.</span><span>If the Evaluator loses or makes unauthorized disclosure of any of the Confidential Information, the Evaluator will immediately notify the Company and take all reasonable steps necessary to retrieve the lost or improperly disclosed Confidential Information.</span></div>
    <div class="clause"><span>16.</span><span>Any notices or delivery required in this Agreement will be deemed completed when hand-delivered, delivered by agent, or seven days after being placed in the post, postage prepaid, to the parties at the addresses contained in this Agreement or as the parties may later designate in writing.</span></div>
    <div class="clause tight"><span>17.</span><span>The addresses for any notice to be delivered to any of the parties to this Agreement are as follows:</span></div>
    <div style="margin-left:13px;margin-bottom:6px">
      <div class="sub tight"><span>a.</span><span>Name: ACME<br>Address: 1510 Cedar Row, Lakeview, MI 49000, USA</span></div>
      <div class="sub tight"><span>b.</span><span>Name: COMPANY NAME<br>Address: COMPANY ADDRESS</span></div>
    </div>
    <p class="heading underline indent">Representations</p>
    <div class="clause"><span>18.</span><span>In providing the Confidential Information, the Company makes no representations, either expressly or impliedly as to its adequacy, sufficiency, completeness, correctness or its lack of defect of any kind, including any patent or trademark infringement that may result from the use of such information.</span></div>
    <p class="heading underline indent">Further Agreements</p>
    <div class="clause"><span>19.</span><span>In the event that the Evaluator finds that the Invention is worthy of being patented, developed and marketed, the Company and the Evaluator may negotiate an additional agreement to define all their respective rights regarding such patenting, marketing, and development.</span></div>
    <p class="heading underline indent">Termination</p>
    <div class="clause"><span>20.</span><span>Either party may terminate this Agreement by providing written notice to the other party. Except as otherwise provided in this Agreement, all rights and obligations under this Agreement will terminate at that time.</span></div>
  </div>
</section>

<section class="page">
  <svg class="page-art" viewBox="0 0 240 340" aria-hidden="true">
    <circle cx="37" cy="258" r="62" fill="var(--faint)"/>
    <path d="M240,250 Q226,302 190,340 H240Z" fill="var(--light)"/>
    <path d="M0,300 Q100,270 240,330 V340 H0Z" fill="var(--dark)"/>
    <path d="M240,298 Q226,325 205,340 H240Z" fill="var(--black)"/>
  </svg>
  <div class="page-number" style="top:17px">Page 7 of 8</div>
  <div class="page-body" style="top:27px;left:17px;width:210px">
    <div class="clause"><span>31.</span><span>This Agreement will inure to the benefit of and be binding upon the respective heirs, executors, administrators, successors and assigns, as the case may be, of the Company and the Evaluator.</span></div>
    <div class="clause"><span>32.</span><span>This Agreement constitutes the entire agreement between the parties and there are no further items or provisions, either oral or otherwise.</span></div>
  </div>
</section>

<!-- Row 2 -->
<section class="page">
  <svg class="page-art" viewBox="0 0 240 340" aria-hidden="true">
    <circle cx="37" cy="258" r="62" fill="var(--faint)"/>
    <path d="M240,250 Q226,302 190,340 H240Z" fill="var(--light)"/>
    <path d="M0,298 Q100,272 240,330 V340 H0Z" fill="var(--dark)"/>
    <path d="M240,298 Q226,325 205,340 H240Z" fill="var(--black)"/>
  </svg>
  <div class="parties">
    <p class="title" style="margin-bottom:0">THIS NON-DISCLOSUREAGREEMENT</p>
    <p style="margin-bottom:14px">("the Agreement")</p>
    <p style="margin-bottom:17px">dated this________________day of, ___________________.</p>
    <p class="strong" style="margin-bottom:16px">BETWEEN:</p>
    <p style="margin-bottom:14px">ACME of 88 Harbor Lane, CA, 90000, USA<br>(the "Company")</p>
    <p style="margin-bottom:8px">OF THE FIRST PART</p>
    <p class="strong" style="margin-bottom:8px">-AND-</p>
    <p style="margin-bottom:17px;line-height:10.5px">COMPANY NAME of COMPANY ADDRESS<br>(the "Evaluator")</p>
    <p>OF THE SECOND PART</p>
  </div>
</section>

<section class="page">
  <svg class="page-art" viewBox="0 0 240 340" aria-hidden="true">
    <circle cx="37" cy="258" r="62" fill="var(--faint)"/>
    <path d="M240,250 Q226,302 190,340 H240Z" fill="var(--light)"/>
    <path d="M0,298 Q100,272 240,330 V340 H0Z" fill="var(--dark)"/>
    <path d="M240,298 Q226,325 205,340 H240Z" fill="var(--black)"/>
  </svg>
  <div class="page-number">Page 2 of 8</div>
  <div class="page-body" style="left:31px;width:195px">
    <div class="sub"><span>d.</span><span>'Service Information' which includes all data and information relating to the services provided by the Company, including but not limited to, plans, schedules, manpower, inspection, and training information;</span></div>
    <div class="sub"><span>e.</span><span>'Product Information' which includes all specifications for products of the Company as well as work product resulting from or related to work or projects of the Company, of any type or form in any stage of actual or anticipated research and development;</span></div>
    <div class="sub"><span>f.</span><span>'Production Processes' which includes processes used in the creation, production and manufacturing of the work product of the Company, including but not limited to, formulas, patterns, molds, models, methods, techniques, specifications, processes, procedures, equipment, devices, programs, and designs;</span></div>
    <div class="sub"><span>g.</span><span>'Accounting Information' which includes, without limitation, all financial statements, annual reports, balance sheets, company asset information, company liability information, revenue and expense reporting, profit and loss reporting, cash flow reporting, accounts receivable, accounts payable, Company reporting, purchasing information and payroll information of the Company;</span></div>
    <div class="sub"><span>h.</span><span>'Marketing and Development Information' which includes marketing and development plans of the Company, price and cost data, price and fee amounts, pricing and billing policies, quoting procedures, marketing techniques and methods of obtaining business, forecasts and forecast assumptions and volumes, and future plans and potential strategies of the Company which have been or are being discussed;</span></div>
    <div class="sub"><span>i.</span><span>'Computer Technology' which includes all scientific and technical information or material of the Company, pertaining to any machine, appliance or process, including but not limited to, specifications, proposals, models, designs, formulas, test results and reports, analyses, simulation results, tables of operating conditions, materials, components, industrial skills, operating and testing procedures, shop practices, know-how and show-how;</span></div>
    <div class="sub"><span>j.</span><span>'Proprietary Computer Code' which includes all sets of statements, instructions or programs of the Company, whether in human readable or machine readable form, that are expressed, fixed, embodied or stored in any manner and that can be used directly or indirectly in a computer ('Computer Programs'); any report format, design or drawing created or produced by such Computer Programs; and all documentation, design specifications and charts, and operating procedures which support the Computer Programs; and</span></div>
  </div>
</section>

<section class="page">
  <svg class="page-art" viewBox="0 0 240 340" aria-hidden="true">
    <circle cx="37" cy="258" r="62" fill="var(--faint)"/>
    <path d="M240,250 Q226,302 190,340 H240Z" fill="var(--light)"/>
    <path d="M0,298 Q100,272 240,330 V340 H0Z" fill="var(--dark)"/>
    <path d="M240,298 Q226,325 205,340 H240Z" fill="var(--black)"/>
  </svg>
  <div class="page-number">Page 4 of 8</div>
  <div class="page-body">
    <div style="margin-left:13px;margin-bottom:6px">
      <div class="sub tight"><span>b.</span><span>To a third party where the Company has consented in writing to such disclosure; and</span></div>
      <div class="sub tight"><span>c.</span><span>To the extent required by law or by the request or requirement of any judicial, legislative, administrative or other governmental body.</span></div>
    </div>
    <div class="clause"><span>8.</span><span>The Evaluator agrees to retain all Confidential Information at its usual place of business and to store all Confidential Information separate from other information and documents held in the same location. Further, the Confidential Information may not be used, reproduced, transformed, or stored on a computer or device that is accessible to persons to whom disclosure may not be made, as set out in this Agreement.</span></div>
    <p class="heading indent">Non-Solicitation</p>
    <div class="clause"><span>9.</span><span>The Evaluator, its affiliates, subsidiaries and representatives will not, from the date of this Agreement for a period of two years, directly or indirectly solicit for employment or employ any person who is now employed or retained by the Company or any affiliate of the Company without the prior written consent of the Company.</span></div>
    <p class="heading indent">Non-Competition</p>
    <div class="clause"><span>10.</span><span>Other than with the express written consent of the Company, which consent may not be unreasonably withheld, the Evaluator will not, from the date of this Agreement for a period of two years, be directly or indirectly involved with a business, which is indirect competition with the Company in the market for the Invention.</span></div>
    <p class="heading indent">Ownership and Title</p>
    <div class="clause"><span>11.</span><span>Nothing contained in this Agreement will grant to or create in the Evaluator, either expressly or impliedly, any right, title, interest or license in or to the intellectual property of the Company.</span></div>
    <p class="heading indent">Remedies</p>
    <div class="clause"><span>12.</span><span>The Evaluator agrees and acknowledges that the Confidential Information is of a proprietary and confidential nature and that any disclosure of the Confidential Information to a third party in breach of this Agreement cannot be reasonably or adequately compensated for in money damages and would cause irreparable injury to the Company. Accordingly, the Evaluator agrees that the Company is entitled to, in addition to all other rights and remedies available to it at law or in equity, an injunction restraining the Evaluator, any of its personnel, and any agents of the Evaluator, from directly or indirectly committing or engaging in any act restricted by this Agreement in relation to the Confidential Information.</span></div>
    <p class="heading indent">Return of Confidential Information</p>
    <div class="clause"><span>13.</span><span>The Company may at any time request the return of all Confidential Information from the Evaluator. Upon the request of the Company, or in the event that the Evaluator ceases to require use of the Confidential Information, or upon the expiration or termination of this Agreement, the Evaluator will:</span></div>
  </div>
</section>

<section class="page">
  <svg class="page-art" viewBox="0 0 240 340" aria-hidden="true">
    <circle cx="37" cy="258" r="62" fill="var(--faint)"/>
    <path d="M240,250 Q226,302 190,340 H240Z" fill="var(--light)"/>
    <path d="M0,298 Q100,272 240,330 V340 H0Z" fill="var(--dark)"/>
    <path d="M240,298 Q226,325 205,340 H240Z" fill="var(--black)"/>
  </svg>
  <div class="page-number" style="top:16px">Page 6 of 8</div>
  <div class="page-body" style="top:27px;left:20px;width:200px">
    <p class="heading underline" style="margin-left:11px">Assignment</p>
    <div class="clause"><span>21.</span><span>Except where a party has changed its corporate name or merged with another corporation, this Agreement may not be assigned or otherwise transferred by either party in whole or part without the prior written consent of the other party to this Agreement.</span></div>
    <p class="heading underline indent">Amendments</p>
    <div class="clause"><span>22.</span><span>This Agreement may only be amended or modified by a written instrument executed by both the Company and the Evaluator.</span></div>
    <p class="heading underline indent">Governing Law</p>
    <div class="clause"><span>23.</span><span>This Agreement will be construed in accordance with and governed by the laws of the State of Michigan.</span></div>
    <p class="heading underline indent">General Provisions</p>
    <div class="clause"><span>24.</span><span>Time is of the essence in this Agreement.25. This Agreement may be executed in counterpart.</span></div>
    <div class="clause"><span>26.</span><span>Headings are inserted for the convenience of the parties only and are not to be considered when interpreting this Agreement. Words in the singular mean and include the plural and vice versa. Words in the masculine mean and include the feminine and vice versa.</span></div>
    <div class="clause"><span>27.</span><span>The clauses, paragraphs, and sub paragraphs contained in this Agreement are intended to be read and construed independently of each other. If any part of this Agreement is held to be invalid, this invalidity will not affect the operation of any other part of this Agreement.</span></div>
    <div class="clause"><span>28.</span><span>The Evaluator is liable for all costs, expenses and expenditures including, and without limitation, the complete legal costs incurred by the Company in enforcing this Agreement as a result of any default of this Agreement by the Evaluator.</span></div>
    <div class="clause"><span>29.</span><span>The Company and the Evaluator acknowledge that this Agreement is reasonable, valid and enforceable. However, if a court of competent jurisdiction finds any of the provisions of this Agreement to be too broad to be enforceable, it is the intention of the Company and the Evaluator that such provision be reduced in scope by the court only to the extent deemed necessary by that court to render the provision reasonable and enforceable, bearing in mind that it is the intention of the Evaluator to give the Company the broadest possible protection against disclosure of the Confidential Information.</span></div>
    <div class="clause"><span>30.</span><span>No failure or delay by the Company in exercising any power, right or privilege provided in this Agreement will operate as a waiver, nor will any single or partial exercise of such rights, powers or privileges preclude any further exercise of them or the exercise of any other right, power or privilege provided in this Agreement.</span></div>
  </div>
</section>

<section class="page">
  <svg class="page-art" viewBox="0 0 240 340" aria-hidden="true">
    <circle cx="37" cy="258" r="62" fill="var(--faint)"/>
    <path d="M240,250 Q226,302 190,340 H240Z" fill="var(--light)"/>
    <path d="M0,298 Q100,272 240,330 V340 H0Z" fill="var(--dark)"/>
    <path d="M240,298 Q226,325 205,340 H240Z" fill="var(--black)"/>
  </svg>
  <div class="page-number" style="top:16px">Page 8 of 8</div>
  <p class="witness" style="top:28px"><strong>IN WITNESS WHERE OF</strong> ACME and COMPANY NAME have duly affixed their signatures under hand and seal on this ____________day of ______________, ___________</p>
  <div class="sign-block" style="top:66px">
    <p>ACME</p>
    <p class="sign-line">Per:_________________________(Seal)</p>
  </div>
  <div class="sign-block" style="top:104px">
    <p>COMPANY NAME</p>
    <p class="sign-line">Per:_________________________(Seal)</p>
  </div>
</section>

</main>
</body>
</html>
```